Design for an iOS and Android app managing shopping list

The app allows you to keep manage shopping lists, each shopping list being made of items to buy...
We need a design for the 3 screens of the app:
a) global view showing list of (shopping) list
b) form enabling to edit the name of a (shopping) list
c) detailed view listing the contents/items of a (shopping) list
d) 1 text page [not illustrated]
2 "alerts" items are also to be designed: confirm and error pop ups.
No specific guidelines, nor logo or whatever.
It will be a free app distributed on iOS and Androïd.
We just want to make it looking nice & very usable for end users.

```html
<!DOCTYPE html>
<html lang="en">
<head>
<meta charset="utf-8">
<title>Basketly – Food list</title>
<link rel="stylesheet" href="https://fonts.googleapis.com/css2?family=Montserrat:wght@300;400;600&display=swap">
<style>
  :root {
    --page-bg: #eef0f3;
    --navy: #2e3749;
    --coral: #f4605a;
    --teal: #0bc3cb;
    --white: #ffffff;
    --ink: #2b2f36;
    --divider: #eef0f2;
    --ring: #c9ccd1;
    --tick: #3ccb6a;
    --tick-ring: #9fe0b4;
  }
  * { box-sizing: border-box; margin: 0; padding: 0; }
  html, body {
    width: 862px; height: 1200px; overflow: hidden;
    background: var(--page-bg);
    font-family: "Montserrat", sans-serif;
  }
  .app-screen {
    position: absolute; left: 94px; top: 0;
    width: 674px; height: 1200px;
    background: var(--white);
    display: flex; flex-direction: column;
  }
  .top-bar {
    height: 93px; background: var(--navy);
    display: flex; align-items: center; padding-left: 30px; gap: 22px;
  }
  .app-name {
    color: var(--white); font-weight: 600; font-size: 34px; letter-spacing: 0.5px;
  }
  .list-header {
    height: 135px; background: var(--coral); color: var(--white);
    display: flex; align-items: center; padding: 0 30px 0 32px;
  }
  .list-title { font-weight: 300; font-size: 50px; margin-left: 26px; flex: 1; }
  .header-actions { display: flex; gap: 34px; align-items: center; }
  .section-bar {
    height: 70px; display: flex; align-items: center; justify-content: space-between;
    padding: 0 33px; color: var(--white); font-weight: 600; font-size: 33px;
  }
  .section-bar.pending { background: var(--navy); }
  .section-bar.done { background: var(--teal); height: 71px; }
  .item-list { list-style: none; }
  .item {
    height: 99px; display: flex; align-items: center; padding-left: 33px;
    border-bottom: 2px solid var(--divider);
    font-size: 29px; color: var(--ink); font-weight: 400; letter-spacing: 0.5px;
  }
  .item:last-child { border-bottom: none; }
  .check { width: 58px; height: 58px; margin-right: 27px; flex: none; }
  .item-list.done-items .item:last-child { border-bottom: 2px solid var(--divider); }
</style>
</head>
<body>
<main class="app-screen">
  <header class="top-bar">
    <svg width="40" height="34" viewBox="0 0 40 34" aria-hidden="true">
      <g stroke="#fff" stroke-width="3"><line x1="0" y1="3" x2="40" y2="3"/><line x1="0" y1="17" x2="40" y2="17"/><line x1="0" y1="31" x2="40" y2="31"/></g>
    </svg>
    <span class="app-name">BASKETLY</span>
  </header>

  <section class="list-header">
    <svg width="22" height="38" viewBox="0 0 22 38" aria-hidden="true">
      <polyline points="19,3 4,19 19,35" fill="none" stroke="#fff" stroke-width="3.5"/>
    </svg>
    <h1 class="list-title">Food</h1>
    <div class="header-actions">
      <svg width="38" height="38" viewBox="0 0 38 38" aria-label="Edit">
        <path d="M30 3 L35 8 L11 32 L6 27 Z" fill="#fff"/><path d="M5 29 L9 33 L2 36 Z" fill="#fff"/>
      </svg>
      <svg width="42" height="42" viewBox="0 0 42 42" aria-label="Add">
        <g stroke="#fff" stroke-width="3.5"><line x1="21" y1="2" x2="21" y2="40"/><line x1="2" y1="21" x2="40" y2="21"/></g>
      </svg>
    </div>
  </section>

  <div class="section-bar pending"><span>Pending</span><span>5</span></div>
  <ul class="item-list">
    <li class="item"><svg class="check" viewBox="0 0 58 58"><circle cx="29" cy="29" r="27.5" fill="none" stroke="var(--ring)" stroke-width="2"/></svg>Orange</li>
    <li class="item"><svg class="check" viewBox="0 0 58 58"><circle cx="29" cy="29" r="27.5" fill="none" stroke="var(--ring)" stroke-width="2"/></svg>Cheese</li>
    <li class="item"><svg class="check" viewBox="0 0 58 58"><circle cx="29" cy="29" r="27.5" fill="none" stroke="var(--ring)" stroke-width="2"/></svg>Garlic</li>
    <li class="item"><svg class="check" viewBox="0 0 58 58"><circle cx="29" cy="29" r="27.5" fill="none" stroke="var(--ring)" stroke-width="2"/></svg>Bread</li>
    <li class="item"><svg class="check" viewBox="0 0 58 58"><circle cx="29" cy="29" r="27.5" fill="none" stroke="var(--ring)" stroke-width="2"/></svg>Milk</li>
  </ul>

  <div class="section-bar done"><span>Done</span><span>2</span></div>
  <ul class="item-list done-items">
    <li class="item"><svg class="check" viewBox="0 0 58 58"><circle cx="29" cy="29" r="27.5" fill="none" stroke="var(--tick-ring)" stroke-width="2"/><polyline points="15,30 25,40 44,18" fill="none" stroke="var(--tick)" stroke-width="3.5"/></svg>Fish</li>
    <li class="item"><svg class="check" viewBox="0 0 58 58"><circle cx="29" cy="29" r="27.5" fill="none" stroke="var(--tick-ring)" stroke-width="2"/><polyline points="15,30 25,40 44,18" fill="none" stroke="var(--tick)" stroke-width="3.5"/></svg>Banana</li>
  </ul>
</main>
</body>
</html>
```